依頼詳細
最終目的は会員入会ですが、まずは、8/16より開始する『内覧会、体験会』の
集客に焦点をあてた、女性が通ってみたいと思えるような、
折込ちらしをお願いします。

【全体で重視する点】
・一目でフィットネスのチラシがわかるように
・メインのモデル画像は女性(フィットネスらしさ重視)
・キャンペーン内容(8/16~9/30までの入会で9月.10月の月会費が0円)が
はっきりとわかるように、表現はお任せします。
・20~40代女性に向けた

※詳細な資料は、添付いたします。

ワークリンドのチラシ作成は初めての利用になり、
説明不足な点、追加事項等あるかと思いますが、よろしくお願いいたします。

記載項目
資料を添付します。
サイズ
B4
ページ数
両面
希望イメージ
• +5 0 +5
• シンプル
複雑
• 単色
カラフル
• 暗い
明るい
• 日常
高級
• 遊び心
厳粛
• 未来的
伝統的
• 女性的
男性的
希望する色
ロゴ色で使用している、オレンジ
納品ファイル
• 高解像度JPG (.jpg)
• イラストレーター形式 (.ai)
• フォトショップ形式 (.psd)
• PNG形式 (.png)
補足説明
依頼公開後の追記内容
ワークリンドの皆様

ご提案いただきありがとうございます。
弊社がイメージしている内容を追記させていただきます。

①メインとなる女性のイメージは、親しみやすい日本人の女性で
お願いします。イメージ画像添付します。(josei_imege)
②20代から40代の幅広い年齢層の集客を目指しているため
ちらしのどこかに30代もしくは40代女性の写真を入れてください。
③キャッチフレーズは、「カラダ引締めスタート」になります。
④HPのイメージ画像を添付します。
使用している画像の雰囲気を感じていただければ(hp_image)
⑤弊社に近いイメージのちらし「ミルヴァ」様を添付します。(MILVA)

追記点が多くなりましたが、引き続きよろしくお願いします。
ワークリンドの皆様

ご提案いただきありがとうございます。
残り時間わずかとなりますが、

①ちらしのどこかに、カタカナ表記「ルミエフィットネス」といれてください。
②和歌山初と入れている文言は、削除してください。
③ちらし表面に、「初心者オススメ」もしくは「初心者対象」といれてください。

```html
<!DOCTYPE html>
<html lang="ja">
<head>
<meta charset="utf-8">
<title>ルミエフィットネス24 オープン告知</title>
<link rel="stylesheet" href="https://fonts.googleapis.com/css2?family=Noto+Sans+JP:wght@500;700;900&family=M+PLUS+Rounded+1c:wght@800&display=swap">
<style>
:root{
  --pink:#e8336b;
  --red:#e5184a;
  --orange:#f08a1c;
  --orange-deep:#e9661a;
  --teal:#2aa8b8;
  --ink:#333;
  --white:#fff;
  --photo-a:#cfe4ee;
  --photo-b:#9fc3d3;
  --skin:#e9cbb5;
}
*{box-sizing:border-box;margin:0;padding:0}
html,body{width:849px;height:1200px;overflow:hidden;background:var(--white)}
body{font-family:"Noto Sans JP",sans-serif;color:var(--ink)}
.flyer{position:relative;width:849px;height:1200px;overflow:hidden;background:var(--white)}
.gym-photo{position:absolute;left:0;top:0;width:849px;height:720px;background:linear-gradient(160deg,var(--photo-a),var(--photo-b) 70%,#bcd6e0)}
.model-photo{position:absolute;left:470px;top:240px;width:340px;height:460px;border-radius:160px 160px 0 0;background:linear-gradient(180deg,#d9b8a0,var(--skin) 40%,#f4f0ec 70%,#e9e4df)}
.tag{position:absolute;left:28px;background:var(--white);color:var(--pink);font-weight:900;line-height:1;padding:8px 14px;white-space:nowrap}
.tag-space{top:48px;font-size:44px}
.tag-24h{top:128px;font-size:40px}
.tag-gym{top:188px;font-size:40px}
.open-date{position:absolute;left:28px;top:250px;font-size:62px;font-weight:900;color:var(--pink);-webkit-text-stroke:8px var(--white);paint-order:stroke fill;letter-spacing:1px;white-space:nowrap}
.open-date small{font-size:40px;display:inline-block;background:var(--pink);color:var(--white);-webkit-text-stroke:0;border-radius:50%;width:52px;height:52px;text-align:center;line-height:52px;vertical-align:8px;margin-left:6px}
.open-word{position:absolute;left:20px;top:305px;font-family:"M PLUS Rounded 1c",sans-serif;font-weight:800;font-size:160px;color:var(--red);-webkit-text-stroke:12px var(--white);paint-order:stroke fill;letter-spacing:4px}
.beginner-badge{position:absolute;left:640px;top:12px;width:185px;height:185px;border-radius:50%;background:var(--white);display:flex;flex-direction:column;align-items:center;justify-content:center;color:var(--orange-deep);font-weight:900;font-size:27px;line-height:1.3;text-align:center;box-shadow:0 0 0 5px var(--orange) inset}
.beginner-badge svg{margin-top:6px}
.band{position:absolute;left:0;top:650px;width:849px;height:140px}
.catch{position:absolute;left:0;width:849px;top:680px;text-align:center;font-size:46px;font-weight:900;color:var(--white);white-space:nowrap}
.preview{position:absolute;left:0;width:849px;top:800px;text-align:center;color:var(--ink);font-weight:900;font-size:50px;white-space:nowrap}
.preview small{font-size:26px;display:inline-block;background:var(--orange-deep);color:var(--white);border-radius:50%;width:38px;height:38px;line-height:38px;vertical-align:8px}
.preview .sub{font-size:40px;margin-left:10px}
.member-photo{position:absolute;left:0;top:900px;width:212px;height:225px;background:linear-gradient(180deg,#e7e1da,#d5c4b6)}
.campaign-title{position:absolute;left:222px;top:925px;width:282px;height:66px;background:var(--orange);color:var(--white);border-radius:10px;text-align:center;font-weight:900;font-size:22px;line-height:1.2;padding-top:8px;white-space:nowrap}
.campaign-title small{display:block;font-size:15px;font-weight:700}
.fee{position:absolute;top:1002px;width:118px;height:92px;border:3px solid var(--pink);border-radius:8px;text-align:center;color:var(--pink);font-weight:900;font-size:24px;line-height:1.1;padding-top:8px}
.fee small{display:block;font-size:18px;color:var(--ink);font-weight:700}
.fee-sep{left:222px}.fee-oct{left:386px}
.plus{position:absolute;color:var(--orange-deep);font-weight:900;font-size:44px;line-height:1}
.plus-a{left:350px;top:1025px}.plus-b{left:724px;top:1000px}
.free-box{position:absolute;left:516px;top:930px;width:196px;height:175px;background:var(--teal);border-radius:10px;color:var(--white);text-align:center;font-weight:900}
.free-box .was{font-size:30px;text-decoration:line-through;margin-top:10px}
.free-box .now{font-size:100px;line-height:1;font-family:"M PLUS Rounded 1c",sans-serif}
.free-box .now span{font-size:56px}
.water{position:absolute;left:774px;top:920px;width:58px;height:200px;border-radius:29px;background:var(--orange);color:var(--white);writing-mode:vertical-rl;font-weight:900;font-size:19px;display:flex;align-items:center;justify-content:center;line-height:1;white-space:nowrap}
.footer{position:absolute;left:0;top:1132px;width:849px;height:68px;display:flex;align-items:center;justify-content:space-between;padding:0 28px;border-top:2px solid var(--orange)}
.brand .store{font-size:15px;font-weight:700}
.brand .name{font-size:26px;font-weight:900;color:var(--orange-deep)}
.contact{text-align:right}
.contact .url{font-size:17px;font-weight:700}
.contact .tel{font-size:30px;font-weight:900;display:flex;align-items:center;gap:6px}
</style>
</head>
<body>
<div class="flyer">
  <div class="gym-photo" role="img" aria-label="明るいフィットネスジムの室内、トレッドミルで運動する女性たち"></div>
  <div class="model-photo" role="img" aria-label="ガッツポーズをする笑顔の日本人女性モデル"></div>

  <div class="tag tag-space">170坪の大空間</div>
  <div class="tag tag-24h">本格的24h</div>
  <div class="tag tag-gym">フィットネスジム</div>
  <div class="open-date">2018.9.13<small>木</small></div>
  <div class="open-word">OPEN</div>

  <div class="beginner-badge">初心者の方に<br>オススメ
    <svg width="34" height="44" viewBox="0 0 34 44"><path d="M17 10 L1 1 V32 L17 43 Z" fill="#f5d400"/><path d="M17 10 L33 1 V32 L17 43 Z" fill="#1f9c4a"/></svg>
  </div>

  <svg class="band" viewBox="0 0 849 140" preserveAspectRatio="none"><polygon points="0,30 849,0 849,110 0,135" fill="var(--orange)"/></svg>
  <div class="catch">カラダ引き締めスタート！</div>
  <div class="preview">8/16<small>木</small>〜9/12<small>水</small><span class="sub">内覧会 体験会開催</span></div>

  <div class="member-photo" role="img" aria-label="マシンでトレーニングする30代女性"></div>
  <div class="campaign-title">オープニングキャンペーン<small>8/16〜9/12までの入会で</small></div>
  <div class="fee fee-sep"><small>9月分<br>月会費</small>¥3,588</div>
  <div class="plus plus-a">+</div>
  <div class="fee fee-oct"><small>10月分<br>月会費</small>¥5,980</div>
  <div class="free-box"><div class="was">¥9,568</div><div class="now"><span>¥</span>0</div></div>
  <div class="plus plus-b">+</div>
  <div class="water">水素水2ヶ月無料</div>

  <footer class="footer">
    <div class="brand"><div class="store">ルミエフィットネス24 緑ヶ丘店</div><div class="name">LUMIE FITNESS 24</div></div>
    <div class="contact"><div class="url">URL:http://lumie-fit.example</div>
      <div class="tel"><svg width="24" height="24" viewBox="0 0 24 24"><path d="M6 2 L10 6 L8 9 Q10 14 15 16 L18 14 L22 18 L19 22 Q4 20 2 5 Z" fill="var(--ink)"/></svg>073-555-0142</div>
    </div>
  </footer>
</div>
</body>
</html>
```